Logo and website for K-12 Academy- Lumora Pathis Academy

Overview
Lumora Pathis Academy is a new online educational institution based in Ghana & Portugal, offering a K-12 curriculum designed to empower the next generation with academic excellence, leadership skills, and deep-rooted cultural values. The academy emphasizes knowledge, mentorship, leadership, and a strong connection to African heritage.

Objective
Create a meaningful, timeless, and visually compelling logo that:

Represents growth, wisdom, and resilience through the imagery of the Odum Tree.

Symbolizes knowledge and academic pursuit.

Reflects mentorship and leadership development.

Appeals to parents and students alike, exuding trust, strength, and inspiration.

Key Themes
Odum Tree: A powerful symbol in Ghana, representing strength, endurance, and wisdom.

Knowledge: Books, light, open pathways, or abstract symbols of learning.

Mentorship/Leadership: Hands guiding others, rising figures, light leading the way, or interconnected branches.

Ghanaian Heritage: Subtle inclusion of Ghanaian cultural elements (such as color palette or patterns) without overwhelming the global, professional appeal.

Target Audience
Parents and guardians seeking quality education steeped in both academic rigor and cultural values.
Students from kindergarten through high school (ages 4–18).
Stakeholders and partners supporting education initiatives in Africa.

Style & Tone
Professional and Inspirational: Serious but welcoming.
Modern with Cultural Depth: Clean lines, minimal clutter, but with depth and meaning.
Warm and Trustworthy: The logo should evoke feelings of safety, hope, growth, and pride.
Flexible: It should work well in both full-color and monochrome versions, and look good at both large and small scales. Except for color changes and cultural elements, main logo should be able to be adapted to both countries
Color Palette (Suggestions)
Earth tones: Browns, greens — representing the Odum tree and growth
Gold/Yellow: For wisdom, enlightenment, and a nod to Ghana’s national colors.
Deep Red or Burgundy: Representing strength and heritage.
Logo Elements
Tree: Odum tree as the main, central symbol. Book, Light, or Path: Sub-elements to subtly symbolize knowledge and learning.
Mentorship: Perhaps visualized through multiple branches, a larger tree protecting smaller saplings, or guiding light themes.

Deliverables
Primary logo (full-color)
Secondary logo (single-color or black/white version)
Icon or emblem version (simplified for small applications like favicons or social media)
Logo usage guidelines (optional but preferred)

Target Market(s)

K-12 parents

Industry/Entity Type

Education

Coding

Coded - Design and coding required

Number of Pages Required

1 page

Font styles to use
Sans Serif

Requirements
Nice to have
• Inspirations Cultural motifs reimagined in a sleek, contemporary style. Nature-inspired logos that convey growth and resilience.

```html
<!DOCTYPE html>
<html lang="en">
<head>
<meta charset="utf-8">
<title>Lumora Pathis Academy</title>
<link rel="stylesheet" href="https://fonts.googleapis.com/css2?family=Catamaran:wght@300;400;500;600;700&display=swap">
<style>
  :root{
    --white:#ffffff;
    --ink:#111111;
    --light-band:#f1f1f1;
    --mid-band:#d6d6d6;
    --accent:#fa7448;
    --tree-dark:#3a3a2c;
    --tree-green:#5d6b3a;
    --tree-brown:#6d5a48;
  }
  *{box-sizing:border-box;margin:0;padding:0}
  html,body{width:1200px;height:1058px;overflow:hidden}
  body{font-family:"Catamaran",sans-serif;color:var(--ink);background:var(--white);font-weight:400}
  .site-header{height:51px;display:flex;align-items:center;justify-content:space-between;padding:0 28px 0 39px;background:var(--white)}
  .brand{display:flex;align-items:center;gap:12px}
  .brand-mark{width:42px;height:42px;border-radius:50%;background:var(--tree-green)}
  .brand-name{font-size:16.5px;font-weight:600}
  .main-nav{display:flex;gap:13px;font-size:13px}
  .main-nav a{color:var(--ink);text-decoration:none}
  .hero{height:334px;position:relative;display:flex;flex-direction:column;align-items:center;padding-top:113px;color:var(--white);text-align:center}
  .hero-image{position:absolute;inset:0;background:
      radial-gradient(ellipse 28% 55% at 50% 80%, var(--tree-brown), transparent 70%),
      radial-gradient(ellipse 70% 70% at 50% 40%, var(--tree-green), var(--tree-dark) 90%);}
  .hero-image::after{content:"";position:absolute;inset:0;background:rgba(0,0,0,.25)}
  .hero > *:not(.hero-image){position:relative}
  .hero h1{font-size:32px;font-weight:700;line-height:1.1}
  .hero p{font-size:16px;font-weight:300;margin-top:12px}
  .btn{display:inline-block;background:var(--accent);color:var(--white);font-weight:700;font-size:11px;border-radius:16px;padding:7px 14px;text-decoration:none;line-height:1.3}
  .hero .btn{margin-top:12px}
  .container{width:747px;margin:0 auto}
  .mission{height:160px;background:var(--light-band);padding-top:44px}
  h2{font-size:18.5px;font-weight:600;line-height:1.2}
  .mission p{font-size:12px;line-height:20px;margin-top:14px}
  .pillars{height:217px;background:var(--mid-band);padding-top:40px}
  .pillar-grid{display:flex;justify-content:space-between}
  .pillar{width:232px;height:137px;background:var(--white);border-radius:8px;padding:16px 13px}
  .pillar h3{font-size:16px;font-weight:600;line-height:1.2}
  .pillar p{font-size:12px;line-height:20px;margin-top:7px}
  .curriculum{height:140px;background:var(--light-band);padding-top:46px}
  .curriculum .container{display:flex;justify-content:space-between;align-items:flex-start}
  .curriculum p{font-size:12px;line-height:20px;margin-top:16px}
  .site-footer{height:156px;background:var(--mid-band);padding-top:30px}
  .footer-grid{display:flex}
  .footer-col{width:258px}
  .footer-col h4{font-size:15.5px;font-weight:600;line-height:1.2;margin-bottom:7px}
  .footer-col p{font-size:12px;line-height:20px}
  .footer-col a{color:var(--ink)}
  .quick-links{list-style:none;font-size:12px;line-height:26.5px;margin-top:-5px}
</style>
</head>
<body>
  <header class="site-header">
    <div class="brand">
      <span class="brand-mark"></span>
      <span class="brand-name">Lumora Pathis Academy</span>
    </div>
    <nav class="main-nav">
      <a href="#">Home</a><a href="#">About Us</a><a href="#">Programs</a><a href="#">Admissions</a><a href="#">Contact</a>
    </nav>
  </header>

  <section class="hero">
    <div class="hero-image" role="img" aria-label="Large Odum tree with spreading branches and green canopy"></div>
    <h1>Welcome to Lumora Pathis Academy</h1>
    <p>Fostering Academic Excellence, Leadership, and Cultural Pride</p>
    <a class="btn" href="#">Enroll Now</a>
  </section>

  <section class="mission">
    <div class="container">
      <h2>Our Mission and Vision</h2>
      <p>At Lumora Pathis Academy, we are committed to nurturing future leaders through a holistic education that balances academic rigor with leadership development and a deep appreciation for African cultural values.</p>
    </div>
  </section>

  <section class="pillars">
    <div class="container pillar-grid">
      <article class="pillar">
        <h3>Academic Excellence</h3>
        <p>Our curriculum is designed to challenge and inspire, ensuring students achieve their highest potential.</p>
      </article>
      <article class="pillar">
        <h3>Mentorship &amp; Leadership</h3>
        <p>We provide mentorship programs that cultivate leadership skills and prepare students for future success.</p>
      </article>
      <article class="pillar">
        <h3>Cultural Roots</h3>
        <p>Our education integrates African cultural values, fostering pride and identity in our students.</p>
      </article>
    </div>
  </section>

  <section class="curriculum">
    <div class="container">
      <div>
        <h2>Curriculum Overview</h2>
        <p>Explore our comprehensive K-12 curriculum that balances academics, leadership, and cultural education.</p>
      </div>
      <a class="btn" href="#">Learn More</a>
    </div>
  </section>

  <footer class="site-footer">
    <div class="container footer-grid">
      <div class="footer-col">
        <h4>Contact Us</h4>
        <p>Email: <a href="#">info@lumorapathisacademy.com</a></p>
        <p>Phone: +233 20 555 0142</p>
      </div>
      <div class="footer-col">
        <h4>Social Media</h4>
        <p>Follow us on our social media channels for updates.</p>
      </div>
      <div class="footer-col">
        <h4>Quick Links</h4>
        <ul class="quick-links"><li>Admissions</li><li>Programs</li><li>FAQs</li></ul>
      </div>
    </div>
  </footer>
</body>
</html>
```